http://www.brightmeadowfold.org/

would like someone to rebuild this -http://www.brightmeadowfold.com/ to be more modern and more easily updated

Industry/Entity Type

Non Profit

Coding

Coded - Design and coding required

Colors

Designer to choose colors to be used in the design.

Requirements
Must have
• use of the logo, and a newer design for wordpress to be hosted on Azure and easily updated templates

```html
<!DOCTYPE html>
<html lang="en">
<head>
<meta charset="utf-8">
<title>Bright Meadow Fold</title>
<link href="https://fonts.googleapis.com/css2?family=Mulish:wght@400;600;700;800&display=swap" rel="stylesheet">
<style>
:root{
  --ink:#2b2b3a;
  --plum:#2e2640;
  --teal:#4d7b86;
  --mist:#c6dade;
  --mist2:#cbdbe0;
  --text:#555a60;
  --white:#fff;
}
*{margin:0;padding:0;box-sizing:border-box}
html,body{width:1200px;height:4484px;overflow:hidden}
body{font-family:'Mulish',sans-serif;color:var(--ink);background:var(--white);position:relative}
.btn{position:absolute;background:var(--teal);color:var(--white);font-weight:800;font-size:21px;display:flex;align-items:center;justify-content:center;border-radius:4px;letter-spacing:.5px}
.section-title{position:absolute;left:0;width:1200px;text-align:center;font-weight:800;font-size:38px;letter-spacing:1px;color:var(--ink)}

/* header */
.header{position:absolute;left:0;top:0;width:1200px;height:122px;background:var(--white)}
.brand{position:absolute;left:98px;top:12px;display:flex;align-items:center;gap:14px}
.brand-mark{width:96px;height:96px;border-radius:50%;border:3px solid var(--plum)}
.top-phone{position:absolute;right:94px;top:18px;display:flex;align-items:center;gap:18px;font-size:27px;font-weight:600;color:var(--ink)}
.nav{position:absolute;left:343px;top:75px;display:flex;gap:31px;font-size:16px;color:#444}
.nav .active{font-weight:800;color:var(--ink)}

/* hero */
.hero{position:absolute;left:0;top:122px;width:1200px;height:583px;background:linear-gradient(135deg,#4a3f35 0%,#7a6a58 40%,#5c5c66 70%,#3f3a36 100%)}
.hero-title{position:absolute;top:175px;left:0;width:1200px;text-align:center;color:var(--white);font-weight:800;font-size:57px;letter-spacing:1px}
.hero-sub{position:absolute;top:243px;left:0;width:1200px;text-align:center;color:var(--white);font-size:25px;line-height:36px}
.hero .btn{left:488px;top:334px;width:223px;height:61px;font-size:28px;border-radius:3px}

/* welcome */
.welcome-text{position:absolute;left:105px;top:822px;width:990px;text-align:center;font-size:19px;line-height:36px;color:var(--text)}

/* about */
.about{position:absolute;left:0;top:1118px;width:1200px;height:429px;background:var(--mist)}
.portrait{position:absolute;left:104px;top:52px;width:323px;height:323px;border-radius:50%;border:6px solid var(--plum);background:radial-gradient(circle at 50% 55%,#b9a08e 0%,#8a5f48 45%,#3b2a24 100%)}
.about h2{position:absolute;left:496px;top:66px;font-size:38px;font-weight:800;letter-spacing:1px}
.about p{position:absolute;left:497px;top:127px;width:608px;font-size:18px;line-height:36px;color:var(--text);text-align:justify}

/* projects */
.doc{position:absolute;background:linear-gradient(180deg,#f6f5f2,#e4e2de);border:2px solid #c9c6c0}
.doc-dark{background:linear-gradient(180deg,#4b4558 0%,#6d6a72 30%,#828085 100%);border:none}
.doc-caption{position:absolute;left:10px;right:10px;top:142px;text-align:center;color:var(--white);font-size:22px;line-height:38px;font-weight:600}

/* media */
.media{position:absolute;left:0;top:2322px;width:1200px;height:688px;background:var(--plum)}
.media .section-title{color:var(--white);top:50px}
.media-hero{position:absolute;left:85px;top:145px;width:492px;height:404px;background:linear-gradient(160deg,#c9c3be 0%,#8d6f8a 45%,#b8a9b6 100%)}
.media-hero-bar{position:absolute;left:0;bottom:0;width:492px;height:93px;background:rgba(77,123,134,.9);color:var(--white);padding:12px 17px}
.media-hero-bar h3{font-size:22px;font-weight:800;letter-spacing:.5px}
.meta{display:flex;align-items:center;gap:10px;font-size:15px;white-space:nowrap}
.meta .sep{width:1px;height:22px;background:currentColor;opacity:.7}
.arrows{position:absolute;right:27px;bottom:17px;display:flex;gap:10px}
.arrows span{width:29px;height:29px;border-radius:50%;background:var(--white);display:flex;align-items:center;justify-content:center}
.thumb{position:absolute;left:599px;width:194px;height:190px}
.post{position:absolute;left:812px;width:296px;color:var(--white)}
.post .meta{font-size:13px;gap:8px}
.post h4{font-size:21px;font-weight:800;margin:10px 0 12px;white-space:nowrap}
.post p{font-size:13px;line-height:22px;text-align:justify;opacity:.9}
.post .more{font-size:15px;margin-top:12px;font-weight:600}
.btn-outline{position:absolute;left:514px;top:598px;width:172px;height:54px;border:2px solid var(--white);border-radius:3px;color:var(--white);font-size:22px;font-weight:700;display:flex;align-items:center;justify-content:center}

/* what's new */
.news h2{position:absolute;left:89px;top:3072px;font-size:38px;font-weight:800;letter-spacing:1px}
.news p{position:absolute;left:89px;top:3137px;width:490px;font-size:15px;line-height:33px;color:var(--text);text-align:justify}
.news-photo{position:absolute;left:796px;top:3069px;width:312px;height:312px;border-radius:50%;border:6px solid var(--plum);background:radial-gradient(circle at 45% 55%,#6f6a72 0%,#4d4855 50%,#2b2733 100%)}

/* contact */
.contact{position:absolute;left:0;top:3439px;width:1200px;height:907px;background:var(--mist2)}
.contact-icon{position:absolute;width:140px;height:140px;border-radius:50%;background:var(--white);border:5px solid var(--plum);display:flex;align-items:center;justify-content:center}
.contact-line{position:absolute;width:400px;text-align:center;font-size:17px;line-height:28px;color:var(--ink)}
.field{position:absolute;background:var(--white);border:1px solid #d6dde0;border-radius:3px;font-size:16px;color:#666;padding:21px 11px 0}
.contact .btn{left:512px;top:796px;width:176px;height:56px}

/* footer */
.footer{position:absolute;left:0;top:4346px;width:1200px;height:138px;background:var(--plum);color:var(--white)}
.footer-nav{position:absolute;top:50px;left:0;width:1200px;display:flex;justify-content:center;gap:34px;font-size:17px;font-weight:700}
.copyright{position:absolute;top:90px;left:0;width:1200px;text-align:center;font-size:15px}
</style>
</head>
<body>

<header class="header">
  <div class="brand">
    <div class="brand-mark"></div>
  </div>
  <div class="top-phone">
    <svg width="34" height="34" viewBox="0 0 34 34"><rect width="34" height="34" rx="6" fill="#1b1b22"/><path d="M11 8c1.2-.6 2.2 0 2.8 1l1.5 3c.4.9.1 1.8-.6 2.3l-1.1.8c.8 2 2.4 3.7 4.4 4.6l.8-1.1c.6-.7 1.5-.9 2.3-.5l3 1.5c1 .5 1.5 1.6.9 2.7-.9 1.7-2.6 2.7-4.4 2.3C14.6 25.5 9.4 20.3 8.3 14.2 8 12.3 9.2 9 11 8z" fill="#fff"/></svg>
    <span>1 (555) 014-2260</span>
  </div>
  <nav class="nav">
    <span class="active">Home</span><span>About Us</span><span>Projects</span><span>Newsletters &amp; Reports</span><span>Media</span><span>What's New</span><span>Contact Us</span>
  </nav>
</header>

<section class="hero" role="img" aria-label="Photo of a caregiver pouring drinks for a group of schoolchildren outdoors">
  <h1 class="hero-title">BRIGHT MEADOW FOLD</h1>
  <p class="hero-sub">By your support of $45 a month, you would draw smiles on the faces<br>of widows and orphans of a needy families.</p>
  <div class="btn">DONATION</div>
</section>

<section class="welcome">
  <h2 class="section-title" style="top:752px">WELCOME TO BRIGHT MEADOW FOLD</h2>
  <p class="welcome-text">Then the King will say to those on His right hand, ‘Come, you blessed of My Father, inherit the kingdom prepared for you from the foundation of the world: for I was hungry and you gave Me food; I was thirsty and you gave Me drink; I was a stranger and you took Me in; I was naked and you clothed Me; I was sick and you visited Me; I was in prison and you came to Me.’</p>
  <div class="btn" style="left:510px;top:1003px;width:178px;height:56px">READ MORE</div>
</section>

<section class="about">
  <div class="portrait" role="img" aria-label="Portrait of the organisation's founder"></div>
  <h2>ABOUT US</h2>
  <p>Today the majority of the problems that face our youngest children, boys and girls in Egypt are caused by lack of every day material needs. "Assuredly, I say to you, in-as-much as you did it to one of the least of these my brethren, you did it to Me.' (Mat 25:40)</p>
  <div class="btn" style="left:498px;top:295px;width:187px;height:59px">READ MORE</div>
</section>

<section class="projects">
  <h2 class="section-title" style="top:1597px">OUR PROJECTS</h2>
  <div class="doc" style="left:89px;top:1681px;width:308px;height:490px" role="img" aria-label="Scanned letter of support for a project"></div>
  <div class="doc" style="left:413px;top:1681px;width:374px;height:239px" role="img" aria-label="Scanned church letter"></div>
  <div class="doc" style="left:413px;top:1930px;width:181px;height:241px" role="img" aria-label="Scanned handwritten note"></div>
  <div class="doc" style="left:605px;top:1930px;width:182px;height:241px" role="img" aria-label="Scanned project table"></div>
  <div class="doc doc-dark" style="left:803px;top:1681px;width:307px;height:490px" role="img" aria-label="Scanned project document">
    <p class="doc-caption">Lorem ipsum dolor sit amet, consectetur adipiscing elit, sed do eiusmodtempor incididunt ut labore et dolore magna aliqua. Ut enim ad minim veniam, quis nostrud exercitation</p>
  </div>
  <div class="btn" style="left:524px;top:2207px;width:187px;height:59px">VIEW MORE</div>
</section>

<section class="media">
  <h2 class="section-title">MEDIA</h2>
  <div class="media-hero" role="img" aria-label="Photo of a child receiving a health check">
    <div class="media-hero-bar">
      <h3>LOREM IPSUM DOLOR SIT AMET</h3>
      <div class="meta" style="margin-top:8px">
        <svg width="16" height="16" viewBox="0 0 16 16" fill="none" stroke="#fff" stroke-width="1.4"><rect x="1.5" y="3" width="13" height="11.5"/><path d="M1.5 6.5h13M5 1v4M11 1v4"/></svg>
        <span>12/09/2019</span><span class="sep"></span><span>16 min Read . By &nbsp;Martin</span>
      </div>
      <div class="arrows">
        <span><svg width="10" height="12" viewBox="0 0 10 12"><path d="M7 1L2 6l5 5" stroke="#2e2640" stroke-width="2" fill="none"/></svg></span>
        <span><svg width="10" height="12" viewBox="0 0 10 12"><path d="M3 1l5 5-5 5" stroke="#2e2640" stroke-width="2" fill="none"/></svg></span>
      </div>
    </div>
  </div>
  <div class="thumb" style="top:145px;background:linear-gradient(135deg,#6b4a3a,#b08a72,#4a3328)" role="img" aria-label="Photo of hands joined together"></div>
  <div class="post" style="top:165px">
    <div class="meta">
      <svg width="15" height="15" viewBox="0 0 16 16" fill="none" stroke="#fff" stroke-width="1.4"><rect x="1.5" y="3" width="13" height="11.5"/><path d="M1.5 6.5h13M5 1v4M11 1v4"/></svg>
      <span>12/10/2019</span><span class="sep"></span><span>16 min Read . By &nbsp;Martin</span>
    </div>
    <h4>Lorem ipsum dolor sit amet</h4>
    <p>Lorem ipsum dolor sit amet, consectetur adipiscing elit. Donec sapien sapien, molestie ac convallis vitae, gravida ut ex.</p>
    <div class="more">READ MORE</div>
  </div>
  <div class="thumb" style="top:361px;background:linear-gradient(135deg,#8a6a4a,#c9a77e,#5a4028)" role="img" aria-label="Photo of hands catching water from a tap"></div>
  <div class="post" style="top:378px">
    <div class="meta">
      <svg width="15" height="15" viewBox="0 0 16 16" fill="none" stroke="#fff" stroke-width="1.4"><rect x="1.5" y="3" width="13" height="11.5"/><path d="M1.5 6.5h13M5 1v4M11 1v4"/></svg>
      <span>12/10/2019</span><span class="sep"></span><span>16 min Read . By &nbsp;Martin</span>
    </div>
    <h4>Lorem ipsum dolor sit amet</h4>
    <p>Lorem ipsum dolor sit amet, consectetur adipiscing elit. Donec sapien sapien, molestie ac convallis vitae, gravida ut ex.</p>
    <div class="more" style="font-weight:400">READ MORE</div>
  </div>
  <div class="btn-outline">View more</div>
</section>

<section class="news">
  <h2>WHAT'S NEW</h2>
  <p>Lorem ipsum dolor sit amet, consectetur adipiscing elit, sed do eiusmod tempor incididunt ut labore et dolore magna aliqua. Ut enim ad minim veniam, quis nostrud exercitation ullamco laboris nisi ut aliquip ex ea commodo consequat. Duis aute irure dolor in reprehenderit in voluptate velit esse cillum dolore</p>
  <div class="btn" style="left:91px;top:3324px;width:176px;height:56px">READ MORE</div>
  <div class="news-photo" role="img" aria-label="Photo of families gathered in a village street"></div>
</section>

<section class="contact">
  <h2 class="section-title" style="top:46px">CONTACT US</h2>
  <div class="contact-icon" style="left:108px;top:144px">
    <svg width="40" height="40" viewBox="0 0 24 24"><path d="M6.6 2.5c.8-.4 1.6 0 2 .7l1.8 3.4c.3.7.1 1.4-.4 1.9L8.6 9.7c1.2 2.5 3.2 4.5 5.7 5.7l1.2-1.4c.5-.5 1.2-.7 1.9-.4l3.4 1.8c.7.4 1.1 1.2.7 2-.8 1.9-2.7 3.2-4.6 2.8C10.5 19 5 13.5 3.8 7.1c-.4-1.9.9-3.8 2.8-4.6z" fill="#1b1b22"/></svg>
  </div>
  <div class="contact-icon" style="left:522px;top:144px">
    <svg width="34" height="44" viewBox="0 0 24 32"><path d="M12 1C6 1 1.5 5.5 1.5 11.2 1.5 18.5 12 31 12 31s10.5-12.5 10.5-19.8C22.5 5.5 18 1 12 1z" fill="#1b1b22"/><circle cx="12" cy="11" r="4" fill="#fff"/></svg>
  </div>
  <div class="contact-icon" style="left:900px;top:144px">
    <svg width="52" height="38" viewBox="0 0 52 38"><rect x="0" y="0" width="52" height="38" rx="4" fill="#1b1b22"/><path d="M3 4l23 18L49 4" stroke="#fff" stroke-width="3" fill="none"/></svg>
  </div>
  <div class="contact-line" style="left:-22px;top:310px">1 (555) 014-2260</div>
  <div class="contact-line" style="left:392px;top:310px">P.O. Box 40218<br>Fairbrook, Vermont 05601-0218</div>
  <div class="contact-line" style="left:770px;top:310px">info@brightmeadowfold.org</div>

  <div class="field" style="left:99px;top:419px;width:483px;height:63px">First name</div>
  <div class="field" style="left:636px;top:419px;width:482px;height:63px">Last name</div>
  <div class="field" style="left:99px;top:508px;width:483px;height:63px">Address</div>
  <div class="field" style="left:636px;top:508px;width:482px;height:241px">Messsage</div>
  <div class="field" style="left:99px;top:597px;width:483px;height:63px">Email</div>
  <div class="field" style="left:99px;top:686px;width:483px;height:63px">Phone number</div>
  <div class="btn">SUBMIT</div>
</section>

<footer class="footer">
  <nav class="footer-nav">
    <span>Home</span><span>About Us</span><span>Projects</span><span>Newsletters &amp; Reports</span><span>Media</span><span>What'S New</span><span>Donation</span><span>Contact Us</span>
  </nav>
  <p class="copyright">Copyright © 2019 &nbsp;Bright Meadow Fold . All Rights Reserved.</p>
</footer>

</body>
</html>
```